Hadley & Partners, LLC Business Card 2016

We need a new business card design for a very important trade show coming up.

We are a compliance Consulting Firm. Our clients are stock brokerage firms and investment advisers.

I would like our logo on both sides of the card.

Info in the front of the card shold include:

Logo
First & Last Name
Title
Office #
Cell #
Email
Company Address (42 W. Calloway St., Suite 300 Pasadena, CA 91417

Back of the card should include the logo and url: www.hadleypartnersgroup.com

Target Market(s)

Stock Brokerage Firms and Investment Advisers

Industry/Entity Type

Financial Service

Contact Information for Business Card

Marcus J. Pellew
President
42 W. Calloway St., Suite 300
Pasadena, CA 91417
O 626.555.0147 ext. 204
C 818.555.0193
Email: marcus@hadleypartnersgroup.com
www.hadleypartnersgroup.com

Requirements
Nice to have
• The back of the card could be black with the logo with the white letters.
• I do want the front of the card to at least have the color logo with the black "Hadley & Partners Lettering.

```html
<!DOCTYPE html>
<html lang="en">
<head>
<meta charset="utf-8">
<title>Hadley &amp; Partners — Business Card</title>
<link rel="stylesheet" href="https://fonts.googleapis.com/css2?family=Cinzel:wght@600&family=Marcellus&display=swap">
<style>
  :root {
    --stage: #ece8e4;
    --paper: #ffffff;
    --ink: #1a1a1a;
    --band: #111111;
    --brand-red: #c8231d;
    --red-light: #e8443a;
    --red-dark: #9a0f0a;
    --grey-text: #9a9a9a;
    --body-text: #222222;
  }
  * { box-sizing: border-box; margin: 0; padding: 0; }
  html, body { width: 1200px; height: 450px; overflow: hidden; }
  body {
    background: var(--stage);
    font-family: "Marcellus", serif;
    position: relative;
  }
  .card {
    position: absolute;
    top: 82px;
    width: 500px;
    height: 286px;
    box-shadow: 0 6px 18px rgba(0,0,0,0.18);
    overflow: hidden;
  }
  .card--front { left: 50px; background: var(--paper); }
  .card--back {
    left: 650px;
    background: linear-gradient(100deg, var(--red-light) 0%, var(--brand-red) 55%, var(--red-dark) 100%);
  }

  /* front: brand line */
  .brand {
    position: absolute;
    left: 0; right: 0; top: 42px;
    display: flex;
    align-items: center;
    justify-content: center;
    gap: 16px;
  }
  .brand__mark {
    width: 44px; height: 44px;
    background: var(--brand-red);
  }
  .brand__name {
    font-family: "Cinzel", serif;
    font-weight: 600;
    font-size: 34px;
    letter-spacing: 1px;
    color: var(--ink);
  }

  /* front: name band */
  .rule {
    position: absolute;
    left: 0; right: 0;
    height: 1px;
    background: var(--brand-red);
  }
  .rule--top { top: 128px; }
  .rule--bottom { top: 181px; }
  .name-band {
    position: absolute;
    left: 0; right: 0;
    top: 133px; height: 44px;
    background: var(--band);
    display: flex;
    align-items: center;
    justify-content: center;
    gap: 6px;
  }
  .name-band__name { color: var(--brand-red); font-size: 17px; }
  .name-band__title { color: var(--grey-text); font-size: 12px; padding-top: 3px; }

  /* front: contacts */
  .contacts {
    position: absolute;
    left: 0; right: 0; top: 196px;
    display: flex;
    flex-direction: column;
    align-items: center;
    gap: 4px;
    font-size: 13.5px;
    color: var(--body-text);
  }
  .contacts__row { display: flex; align-items: center; gap: 26px; }
  .contact { display: flex; align-items: center; gap: 8px; line-height: 18px; }
  .contact svg { width: 12px; height: 12px; fill: var(--body-text); flex: none; }

  /* back */
  .back-brand {
    position: absolute;
    left: 0; right: 0; top: 100px;
    display: flex;
    align-items: center;
    justify-content: center;
    gap: 14px;
  }
  .back-brand__mark { width: 40px; height: 40px; background: var(--paper); }
  .back-brand__name {
    font-family: "Cinzel", serif;
    font-weight: 600;
    font-size: 32px;
    letter-spacing: 1px;
    color: var(--paper);
  }
  .back-url {
    position: absolute;
    left: 0; right: 0; top: 200px;
    text-align: center;
    color: var(--paper);
    font-size: 14px;
    letter-spacing: 0.3px;
  }
</style>
</head>
<body>

<section class="card card--front" aria-label="Card front">
  <div class="brand">
    <span class="brand__mark" aria-hidden="true"></span>
    <span class="brand__name">Hadley &amp; Partners</span>
  </div>

  <div class="rule rule--top"></div>
  <div class="name-band">
    <span class="name-band__name">Your Name,</span>
    <span class="name-band__title">Designation</span>
  </div>
  <div class="rule rule--bottom"></div>

  <div class="contacts">
    <div class="contacts__row">
      <span class="contact">
        <svg viewBox="0 0 24 24" aria-hidden="true"><path d="M6.6 10.8a15.2 15.2 0 0 0 6.6 6.6l2.2-2.2a1 1 0 0 1 1-.25 11.4 11.4 0 0 0 3.6.57 1 1 0 0 1 1 1V20a1 1 0 0 1-1 1A17 17 0 0 1 3 4a1 1 0 0 1 1-1h3.5a1 1 0 0 1 1 1c0 1.25.2 2.45.57 3.57a1 1 0 0 1-.25 1z"/></svg>
        123-456-7890
      </span>
      <span class="contact">
        <svg viewBox="0 0 24 24" aria-hidden="true"><path d="M7 1h10a2 2 0 0 1 2 2v18a2 2 0 0 1-2 2H7a2 2 0 0 1-2-2V3a2 2 0 0 1 2-2zm0 3v13h10V4zm5 15a1 1 0 1 0 0 2 1 1 0 0 0 0-2z"/></svg>
        +91-123-456-7890
      </span>
    </div>
    <span class="contact">
      <svg viewBox="0 0 24 24" aria-hidden="true"><path d="M2 6a2 2 0 0 1 2-2h16a2 2 0 0 1 2 2v12a2 2 0 0 1-2 2H4a2 2 0 0 1-2-2zm2 .5V8l8 5 8-5V6.5l-8 5z"/></svg>
      hello@hadleypartnersmail.com
    </span>
    <span class="contact">
      <svg viewBox="0 0 24 24" aria-hidden="true"><path d="M12 2a10 10 0 1 0 0 20 10 10 0 0 0 0-20zm6.9 6h-3a15 15 0 0 0-1.3-3.9A8 8 0 0 1 18.9 8zM12 4c.8 1.2 1.5 2.5 1.9 4h-3.8c.4-1.5 1.1-2.8 1.9-4zM4.3 14a8 8 0 0 1 0-4h3.4a16 16 0 0 0 0 4zm.8 2h3a15 15 0 0 0 1.3 3.9A8 8 0 0 1 5.1 16zm3-8h-3a8 8 0 0 1 4.3-3.9A15 15 0 0 0 8.1 8zM12 20c-.8-1.2-1.5-2.5-1.9-4h3.8c-.4 1.5-1.1 2.8-1.9 4zm2.3-6H9.7a14 14 0 0 1 0-4h4.6a14 14 0 0 1 0 4zm.3 5.9a15 15 0 0 0 1.3-3.9h3a8 8 0 0 1-4.3 3.9zm1.7-5.9a16 16 0 0 0 0-4h3.4a8 8 0 0 1 0 4z"/></svg>
      www.hadleypartnersgroup.com
    </span>
    <span class="contact">
      <svg viewBox="0 0 24 24" aria-hidden="true"><path d="M12 2a7 7 0 0 0-7 7c0 5.2 7 13 7 13s7-7.8 7-13a7 7 0 0 0-7-7zm0 9.5a2.5 2.5 0 1 1 0-5 2.5 2.5 0 0 1 0 5z"/></svg>
      42 W. Calloway St., Suite 300 Pasadena, CA 91417
    </span>
  </div>
</section>

<section class="card card--back" aria-label="Card back">
  <div class="back-brand">
    <span class="back-brand__mark" aria-hidden="true"></span>
    <span class="back-brand__name">Hadley &amp; Partners</span>
  </div>
  <p class="back-url">www.hadleypartnersgroup.com</p>
</section>

</body>
</html>
```